Van sign writing design( calling the best of the best designers)

Hi Guys
Im after a one of a kind wow statement design to print onto my van.I have just started a plumbing a gasfitting company so i want to show case the type of work i can complete.

The plumbing van attached is the exact wow design im after.

The start of the side of the van in orange merging into the blue color
So in the back ground of the orange colour to have flames and with the blue colour to have a realistic water flowing or splash image as attached

Turn my logo into a translucent/ back ground image as shown in the attachment instead of the orange and blue.

Contact number down the bottom between the front and rear wheels 0219384752
Quendo/lumo brightpurse images as i carry a mobile machine and pinglodge.

Target Market(s)

everyone driving by

Colors
0555a3
f37122

Requirements
Must have
• My logo and stated info
Nice to have
• as stated

```html
<!DOCTYPE html>
<html lang="en">
<head>
<meta charset="utf-8">
<title>Pipeway Plumber &amp; Gas – Van Livery</title>
<link rel="stylesheet" href="https://fonts.googleapis.com/css2?family=Arvo:wght@700&family=Montserrat:wght@600;800&display=swap">
<style>
  :root {
    --brand-blue: #0555a3;
    --brand-orange: #f37122;
    --flame-yellow: #f9b21c;
    --deep-blue: #0a4a8c;
    --water-light: #5fb4e6;
    --tyre: #4f4f51;
    --trim-dark: #2b2b2d;
    --glass: #2e2e30;
    --chrome: #c9cacc;
    --tail-red: #a3203f;
    --web-yellow: #f4e21b;
    --white: #ffffff;
    --page: #ffffff;
  }
  html, body {
    margin: 0;
    padding: 0;
    width: 1200px;
    height: 1200px;
    overflow: hidden;
    background: var(--page);
  }
  .livery-sheet {
    display: block;
    width: 1200px;
    height: 1200px;
  }
  .wordmark {
    font-family: "Montserrat", sans-serif;
    font-weight: 800;
  }
  .phone-number {
    font-family: "Montserrat", sans-serif;
    font-weight: 600;
    fill: var(--white);
  }
  .web-address {
    font-family: "Arvo", serif;
    font-weight: 700;
    fill: var(--web-yellow);
  }
  .social-label, .payment-label {
    font-family: "Montserrat", sans-serif;
    font-weight: 600;
    fill: var(--white);
  }
  .social-label { fill: var(--brand-blue); }
  .panel-line {
    fill: none;
    stroke: rgba(40,40,40,0.35);
    stroke-width: 2;
  }
  .tyre { fill: var(--tyre); }
  .rim { fill: var(--white); }
  .rim-spokes { fill: none; stroke: var(--trim-dark); stroke-width: 36; stroke-dasharray: 24 18; }
  .hub { fill: var(--white); stroke: var(--trim-dark); stroke-width: 4; }
  .glass { fill: var(--glass); }
  .trim { fill: var(--trim-dark); }
  .tail-light { fill: var(--tail-red); }
  .reflector { fill: var(--white); }
</style>
</head>
<body>
<svg class="livery-sheet" viewBox="0 0 1920 1920" xmlns="http://www.w3.org/2000/svg" aria-label="Van livery for Pipeway Plumber and Gas: side, front and rear views">
  <defs>
    <linearGradient id="side-body-fill" x1="0" y1="0" x2="1" y2="0">
      <stop offset="0" stop-color="#f38a22"/>
      <stop offset="0.3" stop-color="#f39a20"/>
      <stop offset="0.45" stop-color="#c9743a"/>
      <stop offset="0.55" stop-color="#7a5a78"/>
      <stop offset="0.68" stop-color="#1e5496"/>
      <stop offset="1" stop-color="#0b4f94"/>
    </linearGradient>
    <radialGradient id="flame-glow" cx="0.5" cy="0.5" r="0.5">
      <stop offset="0" stop-color="#fbd23a" stop-opacity="0.9"/>
      <stop offset="1" stop-color="#f39a20" stop-opacity="0"/>
    </radialGradient>
    <radialGradient id="water-glow" cx="0.5" cy="0.5" r="0.5">
      <stop offset="0" stop-color="#8fd0f4" stop-opacity="0.85"/>
      <stop offset="0.6" stop-color="#3b93d4" stop-opacity="0.5"/>
      <stop offset="1" stop-color="#0b4f94" stop-opacity="0"/>
    </radialGradient>
    <linearGradient id="front-flame-fill" x1="0" y1="0" x2="0" y2="1">
      <stop offset="0" stop-color="#f37a1f"/>
      <stop offset="0.5" stop-color="#f9a825"/>
      <stop offset="1" stop-color="#f38a22"/>
    </linearGradient>
    <linearGradient id="rear-water-fill" x1="0" y1="0" x2="0" y2="1">
      <stop offset="0" stop-color="#0555a3" stop-opacity="0"/>
      <stop offset="0.5" stop-color="#3a8fd0" stop-opacity="0.55"/>
      <stop offset="1" stop-color="#8ccbf0" stop-opacity="0.8"/>
    </linearGradient>
    <radialGradient id="headlamp" cx="0.5" cy="0.5" r="0.5">
      <stop offset="0" stop-color="#ffffff"/>
      <stop offset="1" stop-color="#8b8c8f"/>
    </radialGradient>
  </defs>

  <g class="van-side">
    <circle class="trim" cx="528" cy="772" r="142"/>
    <circle class="trim" cx="1437" cy="772" r="142"/>
    <path class="side-body" fill="url(#side-body-fill)" stroke="#999" stroke-width="2"
      d="M240 840 L240 420 L260 400 L430 215 Q470 188 560 182 L1740 165 Q1770 170 1778 200 L1812 440 L1818 720 L1825 812 L1590 815 Q1585 650 1437 632 Q1295 640 1285 815 L680 840 L668 800 Q650 640 528 632 Q400 640 390 800 L385 840 Z"/>
    <rect x="640" y="180" width="520" height="640" fill="url(#flame-glow)" role="img" aria-label="Photographic flames fading from orange into the blue"/>
    <rect x="1000" y="300" width="820" height="540" fill="url(#water-glow)" role="img" aria-label="Photographic splash of blue water across the rear panel"/>
    <circle cx="1620" cy="560" r="150" fill="#c9d4ea" opacity="0.45" role="img" aria-label="Faint brand emblem area"/>
    <path class="glass" d="M330 430 L350 370 L450 268 Q470 232 520 230 L690 230 L660 385 Q655 405 630 408 Z"/>
    <path class="glass" d="M280 400 L326 352 L328 438 L295 435 Q280 430 280 400 Z"/>
    <path class="glass" d="M600 505 L625 462 L683 462 L683 505 Z"/>
    <path class="glass" d="M772 455 L815 455 L840 505 L772 505 Z"/>
    <path class="panel-line" d="M240 520 L1200 520 M760 195 L760 840 M1235 190 L1235 840 M700 210 L660 400 Q650 520 670 650"/>
    <path class="panel-line" d="M780 210 Q770 240 790 270 L850 410 L1735 410 L1735 200"/>
    <rect x="698" y="560" width="44" height="75" class="panel-line"/>
    <path fill="#d6d7d9" stroke="#999" stroke-width="2" d="M240 420 L175 422 L150 445 L130 470 L120 550 L105 600 L110 660 L240 660 Z"/>
    <rect x="195" y="555" width="40" height="75" rx="8" fill="#9a9b9e"/>
    <path fill="#5e5c58" stroke="#888" stroke-width="2" d="M100 750 L110 660 L240 660 L243 830 L228 842 L130 842 L100 840 Z"/>
    <path class="trim" d="M1745 730 L1822 725 L1825 812 L1750 815 Z"/>
    <rect class="tail-light" x="1780" y="448" width="38" height="210" rx="14"/>
    <rect class="reflector" x="1790" y="578" width="24" height="20"/>
    <rect class="reflector" x="1790" y="612" width="24" height="20"/>
    <path fill="none" stroke="#bbb" stroke-width="3" d="M675 842 L675 855 L845 855 L845 842"/>

    <circle class="tyre" cx="528" cy="768" r="130"/>
    <circle class="rim" cx="528" cy="768" r="80"/>
    <circle class="rim-spokes" cx="528" cy="768" r="52"/>
    <circle class="hub" cx="528" cy="768" r="12"/>
    <circle class="tyre" cx="1437" cy="768" r="130"/>
    <circle class="rim" cx="1437" cy="768" r="80"/>
    <circle class="rim-spokes" cx="1437" cy="768" r="52"/>
    <circle class="hub" cx="1437" cy="768" r="12"/>

    <text class="wordmark" x="815" y="278" font-size="70" textLength="912" lengthAdjust="spacingAndGlyphs" fill="var(--white)">PIPEWAY PLUMBER &amp; <tspan fill="var(--brand-orange)">GAS</tspan></text>
    <text class="phone-number" x="815" y="728" font-size="56" textLength="362" lengthAdjust="spacingAndGlyphs">0219 384 752</text>
    <text class="web-address" x="818" y="782" font-size="24" textLength="356" lengthAdjust="spacingAndGlyphs">www.pipewayplumber.co.nz</text>

    <rect x="272" y="462" width="36" height="74" rx="6" fill="var(--white)" stroke="var(--trim-dark)" stroke-width="3"/>
    <text class="social-label" x="316" y="492" font-size="19">Find us on</text>
    <text class="social-label" x="316" y="522" font-size="28">pinglodge</text>

    <text class="payment-label" x="272" y="636" font-size="20">Quendo</text>
    <text class="payment-label" x="272" y="690" font-size="20">lumo</text>
    <text class="payment-label" x="272" y="744" font-size="16">brightpurse</text>
  </g>

  <g class="van-front">
    <rect class="trim" x="80" y="1160" width="70" height="105" rx="16"/>
    <rect class="trim" x="900" y="1160" width="70" height="105" rx="16"/>
    <rect class="tyre" x="145" y="1690" width="105" height="115" rx="20"/>
    <rect class="tyre" x="800" y="1690" width="105" height="115" rx="20"/>
    <path fill="url(#front-flame-fill)" stroke="#b5651d" stroke-width="2"
      d="M135 1385 L175 1080 Q195 975 300 972 L750 972 Q850 975 870 1080 L915 1385 L915 1730 L135 1730 Z"
      role="img" aria-label="Photographic flames across the front of the van"/>
    <path fill="#8f9093" d="M175 1235 L200 1030 Q210 1000 250 998 L800 998 Q840 1000 850 1030 L870 1235 Z"/>
    <path class="glass" d="M200 1205 L222 1040 Q230 1018 260 1018 L440 1018 L455 1035 L590 1035 L605 1018 L790 1018 Q818 1018 826 1040 L848 1205 Q845 1210 830 1210 L215 1210 Q200 1210 200 1205 Z"/>
    <text class="wordmark" x="203" y="1318" font-size="50" textLength="644" lengthAdjust="spacingAndGlyphs" fill="var(--brand-blue)">PIPEWAY PLUMBER &amp; <tspan fill="var(--white)">GAS</tspan></text>
    <ellipse cx="524" cy="1382" rx="34" ry="24" fill="#a9aaad" stroke="#777" stroke-width="3"/>
    <path fill="#8f9093" d="M135 1385 L300 1385 Q295 1480 215 1490 L135 1490 Z"/>
    <path fill="#8f9093" d="M915 1385 L750 1385 Q755 1480 835 1490 L915 1490 Z"/>
    <ellipse cx="215" cy="1440" rx="75" ry="45" fill="url(#headlamp)"/>
    <ellipse cx="835" cy="1440" rx="75" ry="45" fill="url(#headlamp)"/>
    <path fill="var(--chrome)" stroke="#666" stroke-width="3" d="M300 1402 L750 1402 L735 1492 L315 1492 Z"/>
    <path class="trim" d="M325 1420 L725 1420 L718 1440 L332 1440 Z M335 1458 L715 1458 L708 1478 L342 1478 Z"/>
    <path class="trim" d="M140 1500 L910 1500 L910 1700 L140 1700 Z"/>
    <rect x="260" y="1575" width="525" height="75" fill="#3d3d3f" stroke="#666" stroke-width="3"/>
    <rect x="340" y="1598" width="370" height="20" rx="10" fill="#58585a"/>
    <rect x="260" y="1700" width="525" height="32" fill="url(#front-flame-fill)" role="img" aria-label="Flame band along the front valance"/>
  </g>

  <g class="van-rear">
    <rect class="trim" x="985" y="1140" width="68" height="90" rx="14"/>
    <rect class="trim" x="1795" y="1140" width="65" height="90" rx="14"/>
    <rect class="tyre" x="1055" y="1690" width="100" height="115" rx="20"/>
    <rect class="tyre" x="1690" y="1690" width="103" height="115" rx="20"/>
    <path fill="var(--brand-blue)" stroke="#0a3d75" stroke-width="2"
      d="M1055 1600 L1090 1060 Q1110 978 1200 975 L1650 975 Q1740 978 1760 1060 L1795 1600 Z"/>
    <rect x="1365" y="985" width="115" height="22" rx="10" class="tail-light"/>
    <rect x="1060" y="1150" width="730" height="450" fill="url(#rear-water-fill)" role="img" aria-label="Photographic water splash rising across the rear doors"/>
    <circle cx="1640" cy="1360" r="130" fill="#c9d4ea" opacity="0.45" role="img" aria-label="Faint brand emblem area"/>
    <path class="panel-line" style="stroke:rgba(0,0,0,0.25)" d="M1145 1110 Q1150 1040 1210 1040 L1640 1040 Q1700 1040 1705 1110 L1700 1240 Q1690 1252 1670 1252 L1180 1252 Q1150 1252 1148 1240 Z M1425 1010 L1425 1600"/>
    <text class="wordmark" x="1152" y="1068" font-size="40" textLength="540" lengthAdjust="spacingAndGlyphs" fill="var(--brand-orange)">PIPEWAY PLUMBER &amp; <tspan fill="var(--white)">GAS</tspan></text>
    <ellipse cx="1422" cy="1326" rx="34" ry="24" fill="#a9aaad" stroke="#777" stroke-width="3"/>
    <rect class="trim" x="1255" y="1375" width="340" height="35" rx="8"/>
    <rect class="tail-light" x="1055" y="1285" width="50" height="235" rx="18"/>
    <rect class="tail-light" x="1745" y="1285" width="50" height="235" rx="18"/>
    <rect class="reflector" x="1058" y="1430" width="42" height="25"/>
    <rect class="reflector" x="1058" y="1470" width="42" height="25"/>
    <rect class="reflector" x="1750" y="1430" width="42" height="25"/>
    <rect class="reflector" x="1750" y="1470" width="42" height="25"/>
    <rect x="1124" y="1375" width="48" height="80" rx="14" fill="#6a3d9a"/>
    <rect x="1180" y="1375" width="48" height="80" rx="14" fill="var(--brand-orange)"/>
    <text class="web-address" x="1230" y="1570" font-size="26" textLength="385" lengthAdjust="spacingAndGlyphs">www.pipewayplumber.co.nz</text>
    <path class="trim" d="M1055 1600 L1795 1600 L1793 1700 Q1790 1735 1760 1735 L1090 1735 Q1058 1735 1055 1700 Z"/>
  </g>
</svg>
</body>
</html>
```